Brightfield Optics seeks updated contemporary business card

Brightfield Optics utilizes advanced technology and we take pride in the modern look and feel of our practice. We like our current card, but it's been four years so it is time for an update.

Target Market(s)

Females 25-45 make the most health care decisions for their family.

Contact Information for Business Card

Clean front. Back with info and with empty space for appointment time or other small note

Requirements
Must have
• Logo
Ridge Marketvale, 28413 E Larkspur Ave
Cedar Terrace Marketvale, 4638 S Dunmore Rd
Call or text: 509-342-1968
email: hello@brightfieldoptics.example
brightfieldoptics.example
Dr Tobias Werring & Associates

```html
<!DOCTYPE html>
<html lang="en">
<head>
<meta charset="utf-8">
<title>Brightfield Optics – Business Card</title>
<link rel="stylesheet" href="https://fonts.googleapis.com/css2?family=Noto+Serif:wght@400;700&display=swap">
<style>
  :root {
    --backdrop: #2b2b2d;
    --navy: #1c2657;
    --card-back-top: #cfe4ec;
    --card-back-mid: #bcd6e2;
    --card-back-blush: #c9c8d6;
    --card-front: #ececec;
    --shadow: rgba(0, 0, 0, 0.45);
  }
  * { margin: 0; padding: 0; box-sizing: border-box; }
  html, body {
    width: 1200px;
    height: 800px;
    overflow: hidden;
    background: var(--backdrop);
  }
  .canvas {
    position: relative;
    width: 1200px;
    height: 800px;
    font-family: "Noto Serif", Georgia, serif;
    color: var(--navy);
  }
  .card {
    position: absolute;
    left: 413px;
    width: 373px;
    height: 213px;
    box-shadow: 0 8px 18px var(--shadow);
    overflow: hidden;
  }
  .card--info { top: 160px; }
  .card--brand {
    top: 425px;
    background: var(--card-front);
  }
  .card__photo {
    position: absolute;
    inset: 0;
    background:
      radial-gradient(ellipse 38% 48% at 49% 53%, var(--card-back-blush) 0%, var(--card-back-mid) 70%, transparent 100%),
      linear-gradient(160deg, var(--card-back-top), var(--card-back-mid));
  }
  .contact {
    position: absolute;
    left: 27px;
    top: 24px;
    width: 240px;
    font-size: 9px;
    line-height: 13px;
    letter-spacing: 0.06em;
  }
  .contact__locations { margin-bottom: 16px; }
  .practitioner {
    position: absolute;
    left: 26px;
    top: 121px;
    font-size: 12px;
    line-height: 15px;
    font-weight: 700;
    letter-spacing: 0.03em;
  }
  .brand-mark {
    position: absolute;
    font-weight: 700;
    color: var(--navy);
    white-space: nowrap;
  }
  .brand-mark--small {
    right: 26px;
    top: 170px;
    font-size: 10px;
  }
  .brand-mark--large {
    left: 0;
    right: 0;
    top: 98px;
    text-align: center;
    font-size: 20px;
  }
</style>
</head>
<body>
  <main class="canvas">
    <section class="card card--info">
      <div class="card__photo" role="img" aria-label="Faded close-up photograph of a human eye in pale blue tones"></div>
      <div class="contact">
        <p class="contact__locations">Ridge Marketvale, 28413 E Larkspur Ave Cedar Terrace Marketvale, 4638 S Dunmore Rd</p>
        <p>Call or text: 509-342-1968</p>
        <p>email: hello@brightfieldoptics.example</p>
        <p>Web: brightfieldoptics.example</p>
      </div>
      <p class="practitioner">Dr Tobias Werring<br>&amp; Associates</p>
      <p class="brand-mark brand-mark--small">Brightfield Optics</p>
    </section>

    <section class="card card--brand">
      <p class="brand-mark brand-mark--large">Brightfield Optics</p>
    </section>
  </main>
</body>
</html>
```